Billboard design - consider what a billboard is

Design a billboard using my logo - Billboard is 6m x 3m
A Billboard is advertising for my company that is on a big sign.

Has to be clean and easy to read, and ideally highlights that we are Residential and Commercial builders.

Keep it clean and easy to read

The contact number for the board is

022 583 7092
www.harbourframeworks.co.nz
info@harbourframeworks.co.nz

Doesnt have to have all contact details if it doesnt fit

Has to catch peoples attention to contact us if they need a builder

Can you please change the sign to be all white writing, with black background ?
Updates

Please consider what a billboard is...

The design needs to be suitable for a billboard..

Target Market(s)

people driving past

Industry/Entity Type

Construction

Logo Text

Wellington Builder, website email address, contact number

Colors
0054AA
0677BA
7BADD7
CADEEF
E8F1F8

Requirements
Must have
• Easy to read
Nice to have
• easy to read, can clearly see contact details

```html
<!DOCTYPE html>
<html lang="en">
<head>
<meta charset="utf-8">
<title>Harbour Frameworks Billboard</title>
<link rel="stylesheet" href="https://fonts.googleapis.com/css2?family=Bebas+Neue&family=Montserrat:wght@700&display=swap">
<style>
  :root {
    --navy: #234d6e;
    --navy-dark: #1d2836;
    --sky: #c5d9ed;
    --mid-blue: #7ba6d4;
    --brand-blue: #4f82c6;
    --steel: #a3aebb;
    --ink: #1f2b38;
    --white: #ffffff;
    --page: #e9edf1;
  }
  html, body {
    margin: 0;
    padding: 0;
    width: 1164px;
    height: 1200px;
    overflow: hidden;
    background: var(--page);
  }
  .stage {
    position: relative;
    width: 1164px;
    height: 1200px;
  }
  .billboard {
    position: absolute;
    left: 0;
    top: 309px;
    width: 1500px;
    height: 750px;
    transform: scale(0.776);
    transform-origin: 0 0;
    background: var(--white);
    overflow: hidden;
    font-family: "Bebas Neue", "Oswald", sans-serif;
  }
  .billboard-shapes {
    position: absolute;
    inset: 0;
  }
  .brand {
    position: absolute;
    left: 75px;
    top: 70px;
    display: flex;
    align-items: center;
    gap: 16px;
  }
  .brand-mark {
    width: 34px;
    height: 34px;
    background: var(--brand-blue);
  }
  .brand-name {
    color: var(--brand-blue);
    font-size: 64px;
    line-height: 0.9;
    letter-spacing: 1px;
  }
  .headline {
    position: absolute;
    left: 640px;
    top: 176px;
    margin: 0;
    color: var(--white);
    font-weight: 400;
    font-size: 150px;
    line-height: 150px;
    letter-spacing: 2px;
  }
  .tagline {
    position: absolute;
    left: 580px;
    right: 40px;
    top: 548px;
    margin: 0;
    text-align: right;
    color: var(--ink);
    font-size: 38px;
    letter-spacing: 3px;
  }
  .phone {
    position: absolute;
    left: 52px;
    top: 590px;
    color: var(--white);
    font-size: 104px;
    letter-spacing: 2px;
    line-height: 1;
  }
  .website {
    position: absolute;
    right: 40px;
    top: 650px;
    color: var(--ink);
    font-family: "Montserrat", "Arial", sans-serif;
    font-weight: 700;
    font-size: 34px;
  }
</style>
</head>
<body>
<div class="stage">
  <div class="billboard">
    <svg class="billboard-shapes" width="1500" height="750" viewBox="0 0 1500 750">
      <defs>
        <linearGradient id="skylineTone" x1="0" y1="0" x2="0" y2="1">
          <stop offset="0" stop-color="#a3aebb"/>
          <stop offset="1" stop-color="#234d6e"/>
        </linearGradient>
      </defs>
      <polygon class="sky-band" points="705,0 1500,0 1500,620 560,620" fill="var(--sky)"/>
      <polygon class="stripe" points="600,620 640,620 590,750 550,750" fill="var(--sky)"/>
      <polygon class="stripe" points="660,620 700,620 650,750 610,750" fill="var(--sky)"/>
      <polygon class="stripe" points="720,620 760,620 710,750 670,750" fill="var(--sky)"/>
      <polygon class="headline-tip" points="500,500 580,500 580,545" fill="var(--navy-dark)"/>
      <polygon class="headline-panel" points="597,105 1500,105 1500,500 500,500" fill="var(--navy)"/>
      <rect class="accent-line" x="580" y="500" width="920" height="18" fill="var(--mid-blue)"/>
      <rect class="skyline-art" x="0" y="250" width="560" height="340" fill="url(#skylineTone)" role="img" aria-label="Illustration of a tower crane above a city skyline"/>
      <polygon class="phone-panel" points="0,560 560,560 560,620 520,750 0,750" fill="var(--navy)"/>
    </svg>

    <div class="brand">
      <span class="brand-mark"></span>
      <span class="brand-name">Harbour<br>Frameworks</span>
    </div>

    <h1 class="headline">Need a builder?<br>We’re ready.</h1>

    <p class="tagline">Full-service construction • Residential &amp; Commercial</p>

    <div class="phone">022 583 7092</div>

    <div class="website">www.harbourframeworks.co.nz</div>
  </div>
</div>
</body>
</html>
```